Lens Harbor Teutonia Website - Photography and Films

We are looking for a design that expresses the friendly, open nature of our company Lens Harbor Teutonia, yet at the same time is professional looking and functional.

Lens Harbor Teutonia is a B2B focused operation that hires out multi-lingual camera crews (and equipment) throughout Germany and Europe. We also produce tv features and coporate films. Our unique selling point is that we are native English speakers who can communicate with our international clients (usually British or American) and organise the logistics of shooting in foreign countries.

For content inspiration, see our current website: http://www.lensharborteutonia.com - however we want to move away from the very simple structure of this site and move towards a layout that displays and allows for frequently updated content (e.g. in the form of a blog).

Here is an example of the kind of clean look we like:
http://www.qrvpixelarchive.com/archive/main/reelsqrv.do#reel=48213760

Please keep within the following specifications:
- We wish to keep our logo (grey/white, font: Glypha) and our company colour red (#C40A0A) as they are.
- Maximum Width 960px, on a large browser-window the design should be centred
- Easily readable font sizes with good contrast
- Provide your design in PSD file format
- Our logo should be graphically displayed in the top left of the header.
- The design should allow space for a video.
- The page should have a clearly recognisable end in the form of a footer.

The following menu items need to be clearly arranged so the viewer is not overwhelmed or confused:
About
Services - Crews / Corporate Shoots / Webcasts / Production Arm / Legal Videography
Recent Productions
Blog
Testimonials
Get a Quote
Contact
Film Library
Showreel
Events
Film Location Guide - Frankfurt / Cologne / Zurich / Helsinki / Amsterdam / London / Paris / Rome / Brussels / Berlin / Munich
Updates

Reason: Hi - thanks very much for your interest in our design project.  We are extending this auction because we haven't had enough time to really focus on the desigs and provide immediate feedback to designers.  We will try to provide timely feedback and are giving you more time to make any adjustments to your designs etc.
Thanks!
Marla

Target Market(s)

Our target customers are males and females between 25 and 55 years (mostly British and American). More important than their demographic though, is their occupation - they are largely communication and design savvy individuals belonging to one of the following three categories: 1)Broadcasters (usually producers for example from the QRV or Horizon Vista TV seeking trustworthy, affordable crews for their foreign shoots).

2) Video Production Companies (seeking a trustworthy, affordable partner company to provide the crews for their own corporate clients).

3) Corporate Communications Specialists (seeking professional producers and crews to facilitate production of company videos or filming of events).

Industry/Entity Type

Camera

Requirements
Must have
• A fresh clean appearance with good use of white space.
Should not have
• Avoid dark heavy colours and designs.
• Avoid designs that would be impractical and could potentially take a long time to load.

```html
<!DOCTYPE html>
<html lang="en">
<head>
<meta charset="utf-8">
<title>Lens Harbor Teutonia</title>
<link href="https://fonts.googleapis.com/css2?family=Arvo:wght@700&family=Cabin:wght@400;600&family=Arimo&display=swap" rel="stylesheet">
<style>
:root{
  --red:#c40a0a;
  --red-dark:#a50808;
  --grey-bg:#cccccc;
  --nav-grey:#dcdcdc;
  --panel-grey:#999999;
  --item-grey:#6a6a6a;
  --footer-grey:#6e6e6e;
  --ink:#111111;
  --white:#ffffff;
}
*{box-sizing:border-box;margin:0;padding:0}
html,body{width:956px;height:1200px;overflow:hidden}
body{background:var(--grey-bg);font-family:"Cabin",sans-serif;color:var(--ink);position:relative}
.page{position:absolute;left:36px;top:39px;width:879px;height:1122px;background:var(--white)}
.abs{position:absolute}

.header{left:47px;top:50px;width:860px;height:423px;background:var(--red)}
.logo{left:66px;top:64px;font-family:"Arvo",serif;font-weight:700;font-size:32px;color:var(--white);letter-spacing:-0.5px}
.toplinks{left:632px;top:52px;width:251px;height:22px;background:var(--red-dark);display:flex;justify-content:center;align-items:center;font-size:11px;color:var(--white);gap:6px}
.toplinks span.sep{opacity:.8}

.nav{left:64px;top:114px;width:823px;height:28px;background:var(--nav-grey);display:flex;font-size:15px}
.nav-item{display:flex;align-items:center;padding:0 16px;border-right:1px solid #b5b5b5;height:100%;color:#222}
.nav-item.active{background:var(--white);font-weight:600;flex:1;justify-content:space-between;border-right:none;padding-right:8px}
.caret{width:0;height:0;border-left:5px solid transparent;border-right:5px solid transparent;border-top:6px solid #222;margin-left:8px}
.caret.up{border-top:none;border-bottom:6px solid #222}
.dropdown{left:708px;top:142px;width:179px;height:125px;background:var(--white);padding:4px 10px 0 27px;font-size:12px}
.dropdown li{list-style:none;height:23.5px;line-height:23px;border-bottom:1px solid #c9c9c9}
.dropdown li:last-child{border-bottom:none}
.dropdown .caret{position:absolute;right:6px;bottom:10px}

.player{left:67px;top:164px;width:523px;height:292px;background:#111}
.player-screen{left:6px;top:6px;width:509px;height:213px;background:linear-gradient(90deg,#2c4f84 0%,#2e6aa8 30%,#3fa3c7 65%,#7fd0e4 100%)}
.player-bar{left:6px;top:219px;width:509px;height:20px;background:#2b2b2b;border-radius:0 0 3px 3px}
.progress{left:20px;top:8px;width:450px;height:4px;background:#555;border-radius:2px}
.progress i{display:block;width:45px;height:4px;background:#ddd;border-radius:2px}
.time{right:8px;top:4px;font-size:9px;color:#ddd;font-family:"Arimo",sans-serif}
.pause{left:8px;top:5px;width:6px;height:9px;border-left:2px solid #aaa;border-right:2px solid #aaa}
.thumbs{left:0;top:244px;width:523px;height:42px;display:flex;align-items:center;padding-left:12px;gap:6px}
.thumb{width:35px;height:30px;border:1px solid #888}
.ctrl{color:#ccc;font-size:11px;width:18px;text-align:center}

.crew-photo{left:622px;top:268px;width:285px;height:205px;background:radial-gradient(circle at 65% 40%,#6e4a2a 0%,#2a2a2a 45%,rgba(196,10,10,0) 75%)}

.headline{left:47px;top:498px;width:560px;font-family:"Arvo",serif;font-weight:700;font-size:33px;line-height:36px;letter-spacing:-0.3px}
.posted{left:47px;top:579px;width:152px;height:18px;background:#f5d8d8;color:var(--red);font-size:12.5px;line-height:18px;padding-left:4px}
.article{left:47px;top:623px;width:552px;font-size:14px;line-height:16.2px;text-align:justify}
.article p{margin-bottom:16px}
.article a{color:var(--red);text-decoration:none}
.tags{left:48px;top:956px;font-size:12.5px;color:#555}
.tags b{color:var(--red);font-weight:400}
.social{left:48px;top:978px;display:flex;gap:22px;font-size:11px;font-family:"Arimo",sans-serif}
.like{border:1px solid #c3c8d6;background:#eef0f6;padding:1px 5px;color:#3b5998}
.count{border:1px solid #bbb;padding:1px 3px;margin-left:5px;color:#333}
.follow{border:1px solid #bbb;background:#f4f4f4;padding:1px 5px;color:#333}
.btn{background:var(--red);color:var(--white);font-size:12px;text-align:center;line-height:18px;height:18px}
.btn.view{left:515px;top:1011px;width:94px}

.divider{left:631px;top:508px;width:1px;height:521px;background:#666}
.team{left:654px;top:506px;display:flex;gap:7px}
.team-photo{width:58px;height:58px;background:linear-gradient(180deg,#d8d8d8,#b8a69a);border:3px solid #eee;outline:1px solid #999}
.team-photo.lead{width:64px;height:66px;border-color:#777}
.welcome{left:654px;top:573px;width:252px;height:46px;background:#707070;color:var(--white);font-size:10px;line-height:12.5px;padding:6px 9px;text-align:justify}
.btn.crew{left:811px;top:634px;width:95px}

.events{left:654px;top:687px;width:252px;height:199px;background:var(--panel-grey);padding:9px 7px}
.event{height:56px;background:var(--item-grey);margin-bottom:7px;display:flex;align-items:center;padding-left:6px}
.event-img{width:44px;height:46px;border:2px solid #ddd;flex:none}
.ev1{background:linear-gradient(135deg,#1a1a4a,#b23a7a,#3a8a3a)}
.ev2{background:linear-gradient(135deg,#2a1a5a,#8a6ac8,#3a2a6a)}
.ev3{background:linear-gradient(135deg,#222,#7a1a1a,#444)}
.event-text{color:var(--white);padding:0 8px 0 8px}
.event-text h3{font-family:"Arvo",serif;font-size:12.5px;font-weight:700;line-height:15px}
.event-text p{font-size:9.5px;line-height:12px;text-align:justify}
.btn.more{left:811px;top:902px;width:95px}

.footer{left:46px;top:1049px;width:861px;height:104px;background:var(--footer-grey);padding:10px 22px;font-family:"Arimo",sans-serif;color:#ddd}
.footer-logo{font-family:"Arvo",serif;font-weight:700;font-size:25px;color:#a9a9a9;margin-bottom:6px}
.footer p{font-size:11px;line-height:14px}
.footer .disclaimer{margin-top:8px}
</style>
</head>
<body>
<div class="page"></div>

<header class="abs header"></header>
<div class="abs logo">lensharborteutonia</div>
<nav class="abs toplinks"><span>About</span><span class="sep">|</span><span>Testimonials</span><span class="sep">|</span><span>Get a Quote</span><span class="sep">|</span><span>Contact</span></nav>

<nav class="abs nav">
  <div class="nav-item">Services <span class="caret"></span></div>
  <div class="nav-item">Recent Productions</div>
  <div class="nav-item">Blog</div>
  <div class="nav-item">Film Library</div>
  <div class="nav-item">Showreel</div>
  <div class="nav-item">Events</div>
  <div class="nav-item active">Film Location Guide <span class="caret up"></span></div>
</nav>
<ul class="abs dropdown">
  <li>Frankfurt</li><li>Cologne</li><li>Zurich</li><li>Helsinki</li><li>Amsterdam</li>
  <span class="caret"></span>
</ul>

<div class="abs player">
  <div class="abs player-screen" role="img" aria-label="Video still: presenter speaking beside a tropical sea title card reading Phenomenal Growth"></div>
  <div class="abs player-bar">
    <div class="abs pause"></div>
    <div class="abs progress"><i></i></div>
    <div class="abs time">1:01</div>
  </div>
  <div class="abs thumbs">
    <span class="ctrl">☰</span><span class="ctrl">|◂</span><span class="ctrl">–</span>
    <div class="thumb" style="background:#c8b030" role="img" aria-label="Video thumbnail"></div>
    <div class="thumb" style="background:#7a9a8a" role="img" aria-label="Video thumbnail"></div>
    <div class="thumb" style="background:#b07030" role="img" aria-label="Video thumbnail"></div>
    <div class="thumb" style="background:#c09050" role="img" aria-label="Video thumbnail"></div>
    <div class="thumb" style="background:#8a4a2a" role="img" aria-label="Video thumbnail"></div>
    <div class="thumb" style="background:#6a7a8a" role="img" aria-label="Video thumbnail"></div>
    <div class="thumb" style="background:#7a6a7a" role="img" aria-label="Video thumbnail"></div>
    <div class="thumb" style="background:#3a4a6a" role="img" aria-label="Video thumbnail"></div>
    <div class="thumb" style="background:#b03020" role="img" aria-label="Video thumbnail"></div>
    <span class="ctrl">+</span><span class="ctrl">▸|</span><span class="ctrl" style="margin-left:10px">▶</span>
  </div>
</div>

<div class="abs crew-photo" role="img" aria-label="Photo of a camera operator with headphones filming with a professional video camera"></div>

<h1 class="abs headline">English speaking camera crews throughout germany and europe</h1>
<div class="abs posted">Posted on 30 October 2010</div>

<article class="abs article">
  <p>We set up Lens Harbor Teutonia to meet the demands of a growing number of TV-producers whose working language is English. This is our Passion! Why else would we keep doing it for over 30 years!</p>
  <p>As a producer, you’re bound to have great ideas…but how do you make them a reality in a country where you can’t speak the language? Partner with us!</p>
  <p>We are native English speakers so nothing gets lost in translation. We’ll catch hold of your vision, and with local know-how, we’ll make it happen.</p>
  <p>No job is too big, too small, too hard, too far away, or too urgent. Try us!</p>
  <p style="text-align:left">We provide camera crews and facilities throughout Germany and Europe<br>We shoot in both PAL and NTSC<br>We edit either in-studio or on the move and we transfer urgent footage via FTP or SNG<br>We are on call 24/7</p>
  <p>To make a no obligation enquiry about any of our services, please call our Frankfurt Headquarters: +49-69-472115 (Toll free from the USA 1-800-555-0147) or click here to <a href="#">get a quote</a>.</p>
</article>

<div class="abs tags"><b>Tagged as :</b> Camera crew, Germany, Europe, PAL, NTSC</div>
<div class="abs social"><span><span class="like">Like</span><span class="count">4</span></span><span class="follow">Follow us on Flitter</span></div>
<div class="abs btn view">View more</div>

<div class="abs divider"></div>

<div class="abs team">
  <div class="team-photo lead" role="img" aria-label="Portrait of the executive producer"></div>
  <div class="team-photo" role="img" aria-label="Portrait of a crew member"></div>
  <div class="team-photo" role="img" aria-label="Portrait of a crew member"></div>
  <div class="team-photo" role="img" aria-label="Portrait of a crew member"></div>
</div>
<div class="abs welcome">Hi, Welcome to LensHarborTeutonia. My name is Conrad Whitmore. I am an Executive Producer. I am looking forward to meeting you soon.</div>
<div class="abs btn crew">Meet Our Crew</div>

<section class="abs events">
  <div class="event"><div class="event-img ev1" role="img" aria-label="Film premiere at night"></div><div class="event-text"><h3>Film Premieres</h3><p>Lorem ipsum dolor sit amet, consectetur adipiscing elit.</p></div></div>
  <div class="event"><div class="event-img ev2" role="img" aria-label="Media event stage"></div><div class="event-text"><h3>Media Events</h3><p>Lorem ipsum dolor sit amet, consectetur adipiscing elit.</p></div></div>
  <div class="event"><div class="event-img ev3" role="img" aria-label="Product launch showroom"></div><div class="event-text"><h3>Product Launches</h3><p>Lorem ipsum dolor sit amet, consectetur adipiscing elit.</p></div></div>
</section>
<div class="abs btn more">More Events</div>

<footer class="abs footer">
  <div class="footer-logo">©lensharborteutonia</div>
  <p>c/o Whitmore Films • Lindenweg 12 • 60311 Frankfurt/Main • Germany • info@lens-harbor-teutonia.com</p>
  <p>Tel.: +49-69-472115 • Toll free from the USA 1-800-555-0147</p>
  <p class="disclaimer">Disclaimer</p>
</footer>
</body>
</html>
```